Plakat-Design für Werbetafel-Design für Fussballplatz
Zielgruppe
IT Consulting Dienstleistungen für Internationale Kunden
Aufgabenstellung
Werbetafel-Design für Fussballplatz. (Logo in groß + Slogan 'THE CODE STEWARDS')
Format: 3,0 x 0,75 m
Druckdatenvorabe anbei.

```html
<!DOCTYPE html>
<html lang="en">
<head>
<meta charset="utf-8">
<title>VALTEROS – Pitch-side Board</title>
<link rel="stylesheet" href="https://fonts.googleapis.com/css2?family=Questrial&family=Lato:wght@400&display=swap">
<style>
  :root {
    --brand-blue: #0396d5;
    --brand-green: #86a92a;
    --ink: #161616;
    --paper: #ffffff;
    --page: #ffffff;
    --frame: #1a1a1a;
  }
  * { margin: 0; padding: 0; box-sizing: border-box; }
  html, body {
    width: 1200px;
    height: 600px;
    overflow: hidden;
    background: var(--page);
  }
  .board {
    position: absolute;
    left: 40px;
    top: 160px;
    width: 1120px;
    height: 280px;
    background: var(--paper);
    border: 1px solid var(--frame);
    overflow: hidden;
  }
  .brand-dot {
    position: absolute;
    left: 36px;
    top: 60px;
    width: 120px;
    height: 120px;
    border-radius: 50%;
    background: var(--brand-blue);
  }
  .brand-name {
    position: absolute;
    left: 184px;
    top: 72px;
    font-family: "Questrial", sans-serif;
    font-size: 84px;
    line-height: 1;
    letter-spacing: 1px;
    color: var(--ink);
  }
  .accent-bar {
    position: absolute;
    left: 0;
    top: 215px;
    width: 332px;
    height: 31px;
    background: var(--brand-blue);
  }
  .slogan {
    position: absolute;
    left: 345px;
    top: 185px;
    width: 538px;
    height: 61px;
    background: var(--brand-green);
    color: var(--paper);
    font-family: "Lato", sans-serif;
    font-size: 46px;
    line-height: 61px;
    text-align: center;
  }
  .corner-decor {
    position: absolute;
    right: 0;
    top: 0;
    width: 255px;
    height: 158px;
    background: linear-gradient(135deg, var(--brand-green) 0%, var(--brand-blue) 100%);
    opacity: 0.85;
  }
</style>
</head>
<body>
  <main class="board">
    <div class="brand-dot" aria-hidden="true"></div>
    <h1 class="brand-name">VALTEROS</h1>
    <div class="accent-bar" aria-hidden="true"></div>
    <p class="slogan">The Code Stewards</p>
    <div class="corner-decor" role="img" aria-label="Scattered blue and green pixel squares decoration"></div>
  </main>
</body>
</html>
```